3D sculpture business needs a website

We have created a cool new way to make customized/personalized sculptures.

We scan you from head to toe, digitize you, and print you into your very own sculpture, charm, pendent, or anything else you can imagine.

We are looking for a starter website, an introduction to the products and service including photos, descriptive text, and contact info. A contact/about page, a blog page and events page.

All pages can be hard coded for content, no database required for this version.

Industry/Entity Type

Events

Requirements
Must have
• HTML5
JQuery
Mobile formatting
Nice to have
• Visual Studio Solution
ASP.Net MVC4
Hosted on Windows Azure

```html
<!DOCTYPE html>
<html lang="en">
<head>
<meta charset="utf-8">
<title>FormaFigure – Sculptures World</title>
<link href="https://fonts.googleapis.com/css2?family=Ubuntu:wght@300;400;500&display=swap" rel="stylesheet">
<style>
:root{
  --blue:#2f80f6;
  --blue-light:#5da2ff;
  --page:#f4f4f4;
  --text:#3a3a3a;
  --muted:#6b6b6b;
  --line:#d4d4d4;
  --band:#dcdcdc;
  --footer:#333333;
  --dark-tab:#2b2b2b;
}
*{box-sizing:border-box;margin:0;padding:0}
html,body{width:1200px;height:1164px;overflow:hidden}
body{font-family:'Ubuntu',sans-serif;background:var(--page);color:var(--text);position:relative}
.abs{position:absolute}

/* header */
.brand{left:157px;top:34px;display:flex;align-items:center;gap:10px;font-size:30px;font-weight:400;color:var(--blue)}
.brand-dot{width:34px;height:34px;border-radius:50%;background:#c9a35a}
.phone{right:157px;top:20px;display:flex;align-items:center;gap:8px;font-size:16px;color:#8a8a8a}
.nav{left:559px;top:55px;height:44px;display:flex;font-size:12px;color:#666}
.nav a{color:inherit;text-decoration:none;padding:0 10px;line-height:44px;text-transform:uppercase}
.nav a.active{background:var(--blue);color:#fff;padding:0 11px 0 15px;border-radius:3px 3px 0 0}

/* hero */
.hero-band{left:0;top:99px;width:1200px;height:397px;background:radial-gradient(ellipse 55% 70% at 50% 50%,#7fb6ff 0%,var(--blue) 70%)}
.hero{left:157px;top:114px;width:886px;height:366px;background:linear-gradient(180deg,#4a3e3e 0%,#8d8d92 45%,#c9ccd2 65%,#8a8287 100%)}
.dots{right:18px;top:14px;display:flex;gap:10px}
.dots span{width:15px;height:15px;border-radius:50%;background:var(--blue)}
.dots span:first-child{background:#1d3a5a;box-shadow:inset 0 0 0 3px var(--blue)}
.caption{left:0;bottom:0;width:100%;height:66px;background:rgba(60,60,60,.55);color:#fff;font-size:15px;line-height:20px;padding:12px 30px 0 31px}

/* thumbs */
.arrow-btn{top:518px;width:27px;height:103px;background:var(--blue);display:flex;align-items:center;justify-content:center}
.thumb{top:518px;width:192px;height:103px}

/* welcome */
h2{font-weight:400;color:var(--blue);font-size:19px}
.welcome-h{left:157px;top:648px}
.welcome-img{left:156px;top:689px;width:238px;height:133px;background:radial-gradient(circle at 55% 45%,#6a6a6a 0%,#2a2a2a 70%)}
.welcome-text{left:407px;top:686px;width:317px;font-size:11.5px;line-height:16.6px;text-align:justify;color:#444}
.more{left:651px;top:799px;width:72px;height:26px;border:1px solid #c3c3c3;border-radius:3px;background:linear-gradient(#fafafa,#dedede);color:var(--blue);font-size:12px;text-align:center;line-height:24px}
.shadow-rule{left:157px;top:843px;width:567px;height:14px;background:radial-gradient(ellipse 50% 100% at 50% 0%,rgba(0,0,0,.12),transparent)}
.vrule{left:747px;top:641px;width:1px;height:336px;background:var(--line)}
.services-h{left:157px;top:866px}
.svc{width:176px;height:28px;border-bottom:1px dashed #bdbdbd;display:flex;align-items:center;gap:14px;font-size:12px;color:#333;padding-left:2px}

/* quick contact */
.qc{left:772px;top:641px;width:270px;height:336px;background:var(--blue);border-radius:3px;overflow:hidden;color:#fff}
.qc h3{position:absolute;left:18px;top:16px;font-weight:400;font-size:21px}
.qc label{position:absolute;left:17px;font-size:11.5px}
.qc .star{position:absolute;left:97px;font-size:10px}
.qc .field{position:absolute;left:108px;width:145px;height:22px;background:#fff;border-radius:3px}
.submit{position:absolute;left:181px;top:271px;width:72px;height:26px;border:1px solid #b9c9e0;border-radius:3px;background:linear-gradient(#fbfbfb,#dde6f2);color:var(--blue);font-size:12px;text-align:center;line-height:24px}
.fold{position:absolute;left:0;bottom:0;width:60px;height:40px}

/* blog strip */
.blog-band{left:0;top:1004px;width:1200px;height:83px;background:var(--band)}
.blog-box{left:157px;top:1014px;width:886px;height:62px;border:1px solid #b9b9b9}
.blog-tab{left:157px;top:1014px}
.blog-title{left:170px;top:1029px;color:#fff;font-size:19px;line-height:18px}
.blog-title small{display:block;font-size:11px;line-height:12px}
.blog-text{left:292px;top:1025px;width:740px;font-size:11.5px;line-height:17px;color:#444}

/* footer */
.footer{left:0;top:1087px;width:1200px;height:77px;background:var(--footer)}
.flinks{left:158px;top:1105px;font-size:11.5px;color:#eee;word-spacing:1px}
.flinks span{margin:0 6px;color:#ccc}
.copy{left:158px;top:1127px;font-size:12px;color:#ddd}
.social{right:158px;top:1101px;display:flex;gap:6px}
.social span{width:19px;height:19px;background:#888;border-radius:2px}
</style>
</head>
<body>

<header>
  <div class="abs brand"><span class="brand-dot"></span>FormaFigure.com</div>
  <div class="abs phone">
    <svg width="32" height="32" viewBox="0 0 32 32" fill="none" stroke="#2f80f6" stroke-width="2"><circle cx="17" cy="15" r="12"/><path d="M6 19c1 5 5 8 10 9" /><path d="M4 18l4 -1 1 3-3 2z" fill="#2f80f6"/></svg>
    4488-555-0142
  </div>
  <nav class="abs nav">
    <a class="active">Home</a><a>About Us</a><a>Services</a><a>Galery</a><a>Blog</a><a>Products</a><a>Contact Us</a>
  </nav>
</header>

<section class="abs hero-band"></section>
<section class="abs hero" role="img" aria-label="Photo of a clear ice sculpture of a winged figure">
  <div class="abs dots"><span></span><span></span><span></span></div>
  <p class="abs caption">Lorem Ipsum is simply dummy text of the printing and typesetting industry. Lorem Ipsum has been the industry's stan-<br>dard dummy text ever since the 1500s,</p>
</section>

<div class="abs arrow-btn" style="left:157px"><svg width="12" height="22" viewBox="0 0 12 22"><path d="M10 2 2 11l8 9" stroke="#fff" stroke-width="2" fill="none"/></svg></div>
<div class="abs thumb" style="left:196px;background:radial-gradient(circle at 55% 50%,#9a9a9a,#111 70%)" role="img" aria-label="Photo of a white printed figure sculpture"></div>
<div class="abs thumb" style="left:401px;background:radial-gradient(circle at 50% 50%,#b8b8b8,#dcdcdc 70%)" role="img" aria-label="Photo of a silver figure pendant"></div>
<div class="abs thumb" style="left:606px;background:radial-gradient(circle at 50% 60%,#d8d8d8,#0a0a0a 60%)" role="img" aria-label="Photo of a white torso sculpture"></div>
<div class="abs thumb" style="left:811px;background:radial-gradient(circle at 50% 50%,#c9a040,#dcdcdc 65%)" role="img" aria-label="Photo of a gold figure charm"></div>
<div class="abs arrow-btn" style="left:1014px"><svg width="12" height="22" viewBox="0 0 12 22"><path d="M2 2l8 9-8 9" stroke="#fff" stroke-width="2" fill="none"/></svg></div>

<main>
  <h2 class="abs welcome-h">Welcome to Sculptures World</h2>
  <div class="abs welcome-img" role="img" aria-label="Photo of a silver charm bracelet with a heart pendant"></div>
  <p class="abs welcome-text">Lorem Ipsum is simply dummy text of the printing and type-setting industry. Lorem Ipsum has been the industry's stan-dard dummy text ever since the 1500s, when an unknown printer took a galley of type and scrambled it to make a type specimen book. It has survived not only five centuries, but also the leap into electronic typesetting, remaining essential-</p>
  <div class="abs more">MORE</div>
  <div class="abs shadow-rule"></div>
  <div class="abs vrule"></div>

  <h2 class="abs services-h">Services</h2>
  <div class="abs svc" style="left:157px;top:895px"><svg width="16" height="13"><path d="M1 7l5 5 9-11" stroke="#2f80f6" stroke-width="3" fill="none"/></svg>Scan and making same toy</div>
  <div class="abs svc" style="left:353px;top:895px"><svg width="16" height="13"><path d="M1 7l5 5 9-11" stroke="#2f80f6" stroke-width="3" fill="none"/></svg>charming</div>
  <div class="abs svc" style="left:548px;top:895px"><svg width="16" height="13"><path d="M1 7l5 5 9-11" stroke="#2f80f6" stroke-width="3" fill="none"/></svg>Scan and making same toy</div>
  <div class="abs svc" style="left:157px;top:923px"><svg width="16" height="13"><path d="M1 7l5 5 9-11" stroke="#2f80f6" stroke-width="3" fill="none"/></svg>Digitizeing</div>
  <div class="abs svc" style="left:353px;top:923px"><svg width="16" height="13"><path d="M1 7l5 5 9-11" stroke="#2f80f6" stroke-width="3" fill="none"/></svg>pendent</div>
  <div class="abs svc" style="left:548px;top:923px"><svg width="16" height="13"><path d="M1 7l5 5 9-11" stroke="#2f80f6" stroke-width="3" fill="none"/></svg>Digitizeing</div>
  <div class="abs svc" style="left:157px;top:951px"><svg width="16" height="13"><path d="M1 7l5 5 9-11" stroke="#2f80f6" stroke-width="3" fill="none"/></svg>Printing sculpture</div>
  <div class="abs svc" style="left:353px;top:951px"><svg width="16" height="13"><path d="M1 7l5 5 9-11" stroke="#2f80f6" stroke-width="3" fill="none"/></svg>Analiysing Images</div>
  <div class="abs svc" style="left:548px;top:951px"><svg width="16" height="13"><path d="M1 7l5 5 9-11" stroke="#2f80f6" stroke-width="3" fill="none"/></svg>Printing sculpture</div>

  <aside class="abs qc">
    <h3>Quick contact</h3>
    <label style="top:75px">Name</label><span class="star" style="top:75px">*</span><span class="field" style="top:69px"></span>
    <label style="top:105px">Phone Number</label><span class="star" style="top:105px">*</span><span class="field" style="top:99px"></span>
    <label style="top:136px">E-mail</label><span class="star" style="top:136px">*</span><span class="field" style="top:130px"></span>
    <label style="top:166px">Services</label><span class="star" style="top:166px">*</span><span class="field" style="top:160px"></span>
    <label style="top:197px">Message</label><span class="star" style="top:197px">*</span><span class="field" style="top:191px;height:68px"></span>
    <div class="submit">SUBMIT</div>
    <svg class="fold" viewBox="0 0 60 40"><path d="M0 0h0L0 40h60z" fill="#f4f4f4"/><path d="M0 0l40 40H0z" fill="#cfd8e6"/></svg>
  </aside>
</main>

<section class="abs blog-band"></section>
<div class="abs blog-box"></div>
<svg class="abs blog-tab" width="126" height="62" viewBox="0 0 126 62"><path d="M0 0h100l26 31-26 31H0z" fill="#2b2b2b"/><circle cx="82" cy="31" r="17" fill="#4aa3f0"/><path d="M74 26h16M74 31h16M74 36h10" stroke="#fff" stroke-width="2"/></svg>
<div class="abs blog-title">Blog<small>post</small></div>
<p class="abs blog-text">Lorem Ipsum is simply dummy text of the printing and typesetting industry. Lorem Ipsum has been the industry's standard dummy text ever since the 1500s, when an unknown printer took a galley</p>

<footer class="abs footer"></footer>
<div class="abs flinks">Home<span>|</span>About Us<span>|</span>Services<span>|</span>Galery<span>|</span>Blog<span>|</span>Products<span>|</span>Contact Us</div>
<div class="abs copy">©2012 Northvale All right Reserved</div>
<div class="abs social"><span></span><span></span><span></span><span></span></div>

</body>
</html>
```